Quimby's Yard & Garden Center Business Card Update

I need an updated Business card design for my Lawn and Garden Center. We do Landscaping installs, Lawn Mowing, Snow Removal and also have a Garden Center Retail Division. I uploaded a few of our previous business cards to give an idea of what we are starting with. The main goal of this update is to simplify and modernize the business card, not all of the services that are on the previous cards has to be on the new one but I would still like to highlight our main services. There is also a sample of our logo that Can be used in the design.

Industry/Entity Type

Landscaping

Contact Information for Business Card

Morris Quimby
Morris@Quimbysyardandgarden.example
Business (555) 201-7784
Cell (555) 318-6092

Colors

Designer to choose colors to be used in the design.

Requirements
Must have
• Services Provided :
• Landscaping
• Lawn Maintenance
• Snow Removal
• Garden Center

```html
<!DOCTYPE html>
<html lang="en">
<head>
<meta charset="utf-8">
<title>Quimby's Yard &amp; Garden Center – Business Card</title>
<link href="https://fonts.googleapis.com/css2?family=Roboto+Condensed:wght@700&family=Overpass:wght@700&family=Roboto:wght@400&display=swap" rel="stylesheet">
<style>
  :root {
    --page: #ffffff;
    --card-edge: #8a8a8a;
    --leaf: #2a5937;
    --fold-dark: #1f1b19;
    --fold-light: #8d8b89;
    --ink-light: #ffffff;
  }
  html, body {
    margin: 0;
    width: 1200px;
    height: 1195px;
    overflow: hidden;
    background: var(--page);
  }
  .sheet {
    position: relative;
    width: 1200px;
    height: 1195px;
  }
  .card {
    position: absolute;
    left: 223px;
    width: 751px;
    height: 458px;
    box-sizing: border-box;
    border: 1px solid var(--card-edge);
    background: var(--page);
    overflow: hidden;
  }
  .card--front { top: 124px; }
  .card--back { top: 609px; }
  .card svg { display: block; width: 100%; height: 100%; }
  .brand-name {
    font-family: "Roboto Condensed", sans-serif;
    font-weight: 700;
    fill: var(--leaf);
  }
  .services {
    font-family: "Roboto Condensed", sans-serif;
    font-weight: 700;
    font-size: 28px;
    fill: var(--ink-light);
  }
  .contact-name {
    font-family: "Overpass", sans-serif;
    font-weight: 700;
    font-size: 40px;
    fill: var(--ink-light);
  }
  .contact-line {
    font-family: "Roboto", sans-serif;
    font-weight: 400;
    font-size: 29px;
    fill: var(--ink-light);
  }
  .icon { fill: var(--ink-light); }
  .icon-stroke { fill: none; stroke: var(--ink-light); stroke-width: 3; }
</style>
</head>
<body>
<div class="sheet">

  <!-- Front -->
  <div class="card card--front">
    <svg viewBox="0 0 1063 649" preserveAspectRatio="none" aria-label="Front of business card">
      <defs>
        <linearGradient id="foldFront" x1="510" y1="0" x2="800" y2="200" gradientUnits="userSpaceOnUse">
          <stop offset="0" stop-color="var(--fold-light)"/>
          <stop offset="0.55" stop-color="var(--fold-dark)"/>
        </linearGradient>
        <linearGradient id="foldFrontLow" x1="899" y1="322" x2="700" y2="330" gradientUnits="userSpaceOnUse">
          <stop offset="0" stop-color="#3b3735"/>
          <stop offset="1" stop-color="var(--fold-dark)"/>
        </linearGradient>
      </defs>
      <polygon class="panel" fill="var(--leaf)" points="772,0 1063,0 1063,649 506,649 899,322"/>
      <polygon fill="url(#foldFront)" points="510,0 772,0 899,322 759,207"/>
      <polygon fill="url(#foldFrontLow)" points="759,207 899,322 506,649"/>

      <circle cx="150" cy="290" r="16" fill="var(--leaf)"/>
      <text class="brand-name" x="180" y="322" font-size="96">Quimby's</text>

      <text class="services" text-anchor="end">
        <tspan x="1009" y="465">Services :</tspan>
        <tspan x="1009" y="500">Landscaping •</tspan>
        <tspan x="1009" y="535">Lawn Maintenance •</tspan>
        <tspan x="1009" y="570">Snow Removal •</tspan>
        <tspan x="1009" y="605">Garden Center •</tspan>
      </text>
    </svg>
  </div>

  <!-- Back -->
  <div class="card card--back">
    <svg viewBox="0 0 1063 649" preserveAspectRatio="none" aria-label="Back of business card">
      <defs>
        <linearGradient id="foldBack" x1="554" y1="0" x2="330" y2="150" gradientUnits="userSpaceOnUse">
          <stop offset="0" stop-color="var(--fold-light)"/>
          <stop offset="0.6" stop-color="var(--fold-dark)"/>
        </linearGradient>
        <linearGradient id="foldBackLow" x1="164" y1="324" x2="330" y2="300" gradientUnits="userSpaceOnUse">
          <stop offset="0" stop-color="#3b3735"/>
          <stop offset="1" stop-color="var(--fold-dark)"/>
        </linearGradient>
      </defs>
      <polygon fill="var(--leaf)" points="554,0 1063,0 1063,649 556,649 308,210"/>
      <polygon fill="url(#foldBack)" points="292,0 554,0 308,210 164,324"/>
      <polygon fill="url(#foldBackLow)" points="164,324 308,210 556,649"/>

      <text class="contact-name" x="1009" y="203" text-anchor="end">Morris Quimby</text>

      <text class="contact-line" x="961" y="275" text-anchor="end">(555) 201-7784</text>
      <g class="phone-icon" transform="translate(975,252)">
        <path class="icon" d="M2 6 Q17 -2 32 6 L30 12 L24 11 L23 7 Q17 5 11 7 L10 11 L4 12 Z"/>
        <rect class="icon" x="6" y="13" width="22" height="16" rx="2"/>
      </g>

      <text class="contact-line" x="961" y="325" text-anchor="end">(555) 318-6092</text>
      <g class="mobile-icon" transform="translate(984,298)">
        <rect class="icon-stroke" x="1.5" y="1.5" width="17" height="30" rx="3"/>
        <circle class="icon" cx="10" cy="26" r="2"/>
      </g>

      <text class="contact-line" x="961" y="377" text-anchor="end">Morris@Quimbysyardandgarden.example</text>
      <g class="mail-icon" transform="translate(975,355)">
        <rect class="icon-stroke" x="1.5" y="1.5" width="30" height="20" rx="2"/>
        <path class="icon-stroke" d="M2 3 L16.5 14 L31 3"/>
      </g>

      <circle cx="48" cy="512" r="11" fill="var(--leaf)"/>
      <text class="brand-name" x="66" y="533" font-size="58">Quimby's</text>
    </svg>
  </div>

</div>
</body>
</html>
```